The Steadfast HEART-Ledger Book Cover

Design a book cover that will eventually be part of an entire brand.
The book title: The Steadfast HEART-ledger
Subtitle: Brotherhood Beyond The Era Of The Rising Daughters.
I want it to look masculine, bold and inviting both online and on the shelf.
As much as it is a book for men. Women will be attracted to it as well. They make up over 60% of my fan base. They may buy it for the men in their life.
I do not have any files to upload as this is a first shot at getting the cover and brand started.
I am known as #TheGuideOfBrothers and a men and relationship expert. My mission is to inspire men to live remarkable lives.
Host of The Sturdy Fellow Hour and Founder of The Sturdy Fellow Venture.
This is my second book and feel that the time could not be better for this material.
I think a classy, even vintage/modern look would be great, but again I am open to ideas.
Gordon Pelletier
Target Market(s)
Men 25-60 in transition. Couples going through breakup, separation or divorce. Men that want to find insights, inner peace and understanding themselves and women at a core level.
Colors
Designer to choose colors to be used in the design.
Requirements
Must have
- Bold, creative, inviting
Nice to have
- Background Image that reflects the overall message
Should not have
- Too much artistic licence making it too busy.

```html
<!DOCTYPE html>
<html lang="en">
<head>
<meta charset="utf-8">
<title>The Steadfast HEART-Ledger — Book Cover</title>
<link rel="stylesheet" href="https://fonts.googleapis.com/css2?family=Bebas+Neue&family=EB+Garamond:wght@400&display=swap">
<style>
  :root {
    --cyan: #00f2f2;
    --ink: #060606;
    --backdrop: #f1f1f1;
  }
  * { box-sizing: border-box; margin: 0; padding: 0; }
  html, body {
    width: 899px; height: 1200px; overflow: hidden;
    background: var(--backdrop);
  }
  .spread {
    position: absolute;
    left: 14px; top: 298px;
    width: 870px; height: 602px;
    display: flex;
    box-shadow: 0 2px 10px rgba(0,0,0,0.12);
  }
  /* back cover */
  .back-cover {
    width: 402px; height: 100%;
    background: var(--ink);
    position: relative;
  }
  .blurb {
    position: absolute;
    left: 44px; top: 54px; width: 316px;
    color: var(--cyan);
    font-family: "EB Garamond", Georgia, serif;
    font-size: 12.6px; line-height: 15.6px;
    text-align: justify;
    hyphens: auto;
  }
  .blurb p + p { margin-top: 15px; }
  /* spine */
  .spine {
    width: 66px; height: 100%;
    background: var(--cyan);
    position: relative;
  }
  .spine-text {
    position: absolute;
    left: 50%; top: 40px;
    transform: translateX(-50%);
    writing-mode: vertical-rl;
    font-family: "Bebas Neue", Impact, sans-serif;
    color: var(--ink);
    white-space: nowrap;
  }
  .spine-title { font-size: 29px; letter-spacing: 0.3px; }
  .spine-author { font-size: 27px; margin-top: 34px; letter-spacing: 1px; }
  /* front cover */
  .front-cover {
    width: 402px; height: 100%;
    background: var(--cyan);
    position: relative;
    overflow: hidden;
    font-family: "Bebas Neue", Impact, sans-serif;
  }
  .title {
    position: absolute;
    left: 30px; top: 24px;
    color: var(--ink);
    font-weight: 400;
    line-height: 0.92;
  }
  .title-line-one { font-size: 60px; word-spacing: 24px; display: block; }
  .title-line-two { font-size: 68px; display: block; letter-spacing: 0.5px; }
  .subtitle-band {
    position: absolute;
    left: 30px; right: 0; top: 151px; height: 28px;
    background: var(--ink);
    color: var(--cyan);
    font-size: 15.5px;
    line-height: 28px;
    padding-left: 8px;
    white-space: nowrap;
  }
  .portrait-art {
    position: absolute;
    left: 34px; top: 196px;
    width: 330px; height: 406px;
    background: linear-gradient(160deg, var(--cyan) 0%, #0b5d5d 45%, var(--ink) 75%);
    border-radius: 150px 150px 0 0;
    clip-path: polygon(0 0, 100% 0, 100% 60%, 62% 72%, 62% 100%, 0 100%);
  }
  .author {
    position: absolute;
    right: 18px; bottom: 22px;
    z-index: 1;
    text-align: right;
    color: var(--ink);
    font-size: 36px;
    line-height: 0.95;
    letter-spacing: 1px;
  }
</style>
</head>
<body>
  <main class="spread">
    <section class="back-cover">
      <div class="blurb">
        <p>Lorem ipsum dolor sit amet, consectetur adipiscing elit. Integer risus ex, pulvinar sit amet lectus at, porta tempor ipsum. In fringilla condimentum augue, a finibus urna dictum condimentum. Vivamus sit amet tortor leo. Nullam varius, nisl vitae placerat pretium, lacus ligula viverra lorem, in posuere mi elit imperdiet turpis. Vivamus ipsum mauris, commodo vitae tempus id, mollis id mauris. Phasellus feugiat massa et eros fringilla aliquam. Maecenas ut iaculis nibh. Aliquam consectetur, leo quis ultricies efficitur, nisl ligula tristique turpis, sed consectetur justo tellus eget massa.</p>
        <p>Nunc ultrices sem dictum sapien faucibus tristique. Donec ut vehicula dolor. Sed molestie mollis lectus, id fermentum elit egestas et. Vivamus quis semper mi. Fusce vehicula fermentum aliquet. Suspendisse potenti. Nullam interdum, lacus nec vehicula luctus, lacus purus ullamcorper sapien, at laoreet justo arcu ut libero.</p>
      </div>
    </section>

    <section class="spine">
      <div class="spine-text">
        <span class="spine-title">The Steadfast HEART-ledger</span>
        <span class="spine-author">Gordon Pelletier</span>
      </div>
    </section>

    <section class="front-cover">
      <h1 class="title">
        <span class="title-line-one">The Steadfast</span>
        <span class="title-line-two">HEART-Ledger</span>
      </h1>
      <div class="subtitle-band">Brotherhood Beyond The Era Of The Rising Daughters.</div>
      <div class="portrait-art" role="img" aria-label="Illustration: black profile silhouette of a man's head facing right, with a cyan inner profile and a female symbol in the mind"></div>
      <p class="author">Gordon<br>Pelletier</p>
    </section>
  </main>
</body>
</html>
```